Signage Design Project

We are a chiropractic clinic that caters mostly to athletes. We've recently purchased the first whole body cryotherapy unit in San Antonio, TX (for commercial use - the SA Comets have a unit for their facility) that we would like to advertise in window signage. Please refer to frostvale.com & chillharbor.com to get more info about this service. Our focus is recovery, injury therapy, performance enhancement, metabolic & immunity boost, rheumatoid diseases & pain management, anti-aging & skin rejuvenation. Window measures approximately 8'8" X 3'2"
We mostly use the horizontal logo format (attached) in black & blue.
Industry/Entity Type
Clinic
Requirements
Must have
- Website: www.kelworthback.com
Logo (attached)
"JUST 3 MINUTES FOR WHOLE BODY RECOVERY"
"Whole Body Cryotherapy"
*recovery
*injury therapy
*performance enhancement
*metabolic & immunity boost
*rheumatoid diseases
*pain management
*anti-aging
*skin rejuvenation
Nice to have
- image of Cryo unit (attached)
image of an athlete(s) similar to the ones attached

```html
<!DOCTYPE html>
<html lang="en">
<head>
<meta charset="utf-8">
<title>Kelworth Sport &amp; Spine – Whole Body Cryotherapy</title>
<link href="https://fonts.googleapis.com/css2?family=Oswald:wght@500;600;700&family=Arimo:wght@400;700&display=swap" rel="stylesheet">
<style>
  :root{
    --brand-blue:#27a7df;
    --sky-blue:#4fc3f2;
    --ink:#1c1c1c;
    --black:#111111;
    --white:#ffffff;
    --pink:#f0789a;
  }
  *{margin:0;padding:0;box-sizing:border-box}
  html,body{width:1200px;height:3287px;overflow:hidden}
  body{background:var(--brand-blue);position:relative;font-family:"Arimo",Arial,sans-serif}
  .sign{position:relative;width:1200px;height:3287px}

  .header{position:absolute;left:0;top:0;width:1200px;height:343px;background:var(--white);border-bottom-left-radius:90px}
  .brand{position:absolute;left:110px;top:70px;display:flex;align-items:center;gap:60px}
  .brand-dot{width:200px;height:200px;border-radius:50%;background:var(--brand-blue)}
  .brand-name{font-family:"Oswald",sans-serif;font-weight:600;color:var(--brand-blue);line-height:1;text-align:center}
  .brand-name .line1{display:block;font-size:110px;letter-spacing:6px}
  .brand-name .line2{display:block;font-size:56px;letter-spacing:4px;margin-top:10px}

  .hero-photo{position:absolute;left:0;top:343px;width:1170px;height:852px;border-top-right-radius:80px;
    background:linear-gradient(100deg,#3b3f47 0%,#6d7785 40%,#c9d2dc 70%,#8e97a3 100%)}

  .headline{position:absolute;left:0;top:1195px;width:1200px;height:348px;text-align:center;color:var(--white);font-family:"Oswald",sans-serif;font-weight:700;text-transform:uppercase}
  .headline .big{display:block;font-size:150px;line-height:1;margin-top:70px;letter-spacing:1px}
  .headline .small{display:block;font-size:74px;line-height:1;margin-top:22px;letter-spacing:1px}

  .therapy-photos{position:absolute;left:0;top:1543px;width:1200px;height:465px;display:flex;gap:12px}
  .therapy-photo{flex:1;height:100%}
  .therapy-photo.neck{background:linear-gradient(135deg,#2a2a2c 0%,#b08c78 55%,#e2c4b1 100%)}
  .therapy-photo.tool{background:linear-gradient(135deg,#4a4541 0%,#c9a592 60%,#d9bca9 100%)}

  .service-bar{position:absolute;left:0;top:2008px;width:1200px;height:114px;background:var(--black);color:var(--sky-blue);font-size:72px;font-weight:700;display:flex;align-items:center;justify-content:center}

  .services-panel{position:absolute;left:0;top:2122px;width:1200px;height:840px;background:var(--white);border-bottom-right-radius:120px}
  .service-list{list-style:none;position:absolute;left:60px;top:55px}
  .service-list li{display:flex;align-items:center;height:94px;font-family:"Oswald",sans-serif;font-weight:600;font-size:64px;color:var(--ink)}
  .service-list svg{width:56px;height:56px;margin-right:22px;flex:none}

  .call-badge{position:absolute;left:806px;top:2600px;width:290px;height:290px;border-radius:50%;background:var(--brand-blue);color:var(--white);text-align:center;font-family:"Oswald",sans-serif;font-weight:700}
  .call-badge .call{display:block;font-size:48px;margin-top:48px;line-height:1}
  .call-badge .now{display:block;font-size:76px;line-height:1;margin-top:6px}
  .phone{position:absolute;left:757px;top:2807px;width:392px;height:70px;background:var(--pink);color:var(--white);font-family:"Oswald",sans-serif;font-weight:600;font-size:56px;line-height:70px;text-align:center}

  .address{position:absolute;left:0;top:2980px;width:1200px;text-align:center;color:var(--white);font-size:58px;line-height:66px}

  .footer{position:absolute;left:0;top:3140px;width:1200px;height:147px;background:var(--black);color:var(--white);font-weight:700;font-size:62px;display:flex;align-items:center;justify-content:center;letter-spacing:1px}
</style>
</head>
<body>
<div class="sign">
  <header class="header">
    <div class="brand">
      <span class="brand-dot"></span>
      <span class="brand-name"><span class="line1">KELWORTH</span><span class="line2">SPORT &amp; SPINE</span></span>
    </div>
  </header>

  <div class="hero-photo" role="img" aria-label="Athlete running with earphones beside a whole body cryotherapy chamber"></div>

  <h1 class="headline"><span class="big">Just 3 Minutes</span><span class="small">For Whole Body Recovery</span></h1>

  <div class="therapy-photos">
    <div class="therapy-photo neck" role="img" aria-label="Practitioner adjusting a patient's neck on a treatment table"></div>
    <div class="therapy-photo tool" role="img" aria-label="Soft tissue tool used on a patient's shoulder"></div>
  </div>

  <div class="service-bar">Whole Body Cryotherapy</div>

  <section class="services-panel">
    <ul class="service-list">
      <li><svg viewBox="0 0 24 24"><polyline points="3,13 9,19 21,4" fill="none" stroke="var(--brand-blue)" stroke-width="3" stroke-linecap="round" stroke-linejoin="round"/></svg>Recovery</li>
      <li><svg viewBox="0 0 24 24"><polyline points="3,13 9,19 21,4" fill="none" stroke="var(--brand-blue)" stroke-width="3" stroke-linecap="round" stroke-linejoin="round"/></svg>Injury therapy</li>
      <li><svg viewBox="0 0 24 24"><polyline points="3,13 9,19 21,4" fill="none" stroke="var(--brand-blue)" stroke-width="3" stroke-linecap="round" stroke-linejoin="round"/></svg>Performance enhancement</li>
      <li><svg viewBox="0 0 24 24"><polyline points="3,13 9,19 21,4" fill="none" stroke="var(--brand-blue)" stroke-width="3" stroke-linecap="round" stroke-linejoin="round"/></svg>Metabolic &amp; immunity boost</li>
      <li><svg viewBox="0 0 24 24"><polyline points="3,13 9,19 21,4" fill="none" stroke="var(--brand-blue)" stroke-width="3" stroke-linecap="round" stroke-linejoin="round"/></svg>Rheumatoid diseases</li>
      <li><svg viewBox="0 0 24 24"><polyline points="3,13 9,19 21,4" fill="none" stroke="var(--brand-blue)" stroke-width="3" stroke-linecap="round" stroke-linejoin="round"/></svg>Pain management</li>
      <li><svg viewBox="0 0 24 24"><polyline points="3,13 9,19 21,4" fill="none" stroke="var(--brand-blue)" stroke-width="3" stroke-linecap="round" stroke-linejoin="round"/></svg>Anti-aging</li>
      <li><svg viewBox="0 0 24 24"><polyline points="3,13 9,19 21,4" fill="none" stroke="var(--brand-blue)" stroke-width="3" stroke-linecap="round" stroke-linejoin="round"/></svg>Skin rejuvenation</li>
    </ul>
    <div class="call-badge"><span class="call">CALL US</span><span class="now">NOW!</span></div>
  </section>
  <div class="phone">210.555.0147</div>

  <address class="address" style="font-style:normal">412 Alder Crest Ste #210<br>San Antonio, TX 78258</address>

  <footer class="footer">www.kelworthback.com</footer>
</div>
</body>
</html>
```